MOSLEN Environmental needs an upgrade to its current business cards design

We need an upgrade to our current business cards design, where the MOSLEN acronym is included, as possible and not being overloaded.
MOSLEN Environmental is an Environmental Consultancy Firm based in Sydney.
We would like to see creative designs different from the standard type of business cards (for example, rounded edges, different to standard size of common business cards.

Target Market(s)

industrial companies (oil & gas, petrochemical, mining, insolvency, finance and manufacturing), developers, architect firms, law firms.

Industry/Entity Type

Business

Contact Information for Business Card

logos (brand and acronym), if they don't appear overloaded.
name
role
name of company (MOSLEN Environmental),
address (Level 3, Suite 3C, 47-49 Dorrigan Lane, Wexmoor, NSW, 2188) landline (02 7314 2986)
mobile (staff member)
email (staff member) and
website (www.moslengreen.example).
Include: Contaminated Land, Site Remediation, Groundwater Assessment, Health and Ecological Risk Assessments, Acid Sulfate Soils, Waste Classification.

Font styles to use
Serif
Sans Serif

Requirements
Must have
• A creative design different to the standard type of business cards.
Nice to have
• Rounded edges
• Different size of business cards rather than the standard size.
Should not have
• Preferable not to use white colour background, unless it is required from a creative design proposed.
• Not an overloaded design.
• Avoid black colours

```html
<!DOCTYPE html>
<html lang="en">
<head>
<meta charset="utf-8">
<title>MOSLEN Environmental — Business Cards</title>
<link rel="stylesheet" href="https://fonts.googleapis.com/css2?family=Montserrat:wght@400;500;700;800&display=swap">
<style>
  :root {
    --backdrop: #2a2a2a;
    --leaf-green: #6ab043;
    --slate: #3f3f3f;
    --white: #ffffff;
    --mist: #d8d8d8;
    --divider: #8a8a8a;
  }
  * { box-sizing: border-box; margin: 0; padding: 0; }
  html, body { width: 1200px; height: 900px; overflow: hidden; }
  body {
    background: var(--backdrop);
    font-family: "Montserrat", sans-serif;
    position: relative;
  }
  .card {
    position: absolute;
    width: 700px;
    height: 400px;
    border-radius: 34px;
  }
  .card--front {
    left: 110px; top: 45px;
    background: var(--leaf-green);
    color: var(--white);
    display: flex; flex-direction: column; align-items: center; justify-content: center;
  }
  .card--back {
    left: 390px; top: 465px;
    background: var(--slate);
    display: flex; align-items: center;
  }
  .brand { text-align: center; font-weight: 800; line-height: 1; }
  .brand__name { font-size: 92px; letter-spacing: 2px; display: block; }
  .brand__sub { font-size: 25px; letter-spacing: 6px; display: block; margin-top: 8px; }
  .card--front .brand { color: var(--white); }
  .services {
    list-style: none; text-align: center; margin-top: 22px;
    font-size: 17px; font-weight: 400; line-height: 1.4;
  }
  .card--back .brand { color: var(--leaf-green); width: 345px; }
  .card--back .brand__name { font-size: 70px; }
  .card--back .brand__sub { font-size: 19px; letter-spacing: 4.5px; }
  .divider { width: 1px; height: 250px; background: var(--divider); }
  .contact { padding-left: 32px; color: var(--mist); font-size: 17px; line-height: 1.45; }
  .contact__name { color: var(--leaf-green); font-size: 27px; font-weight: 500; letter-spacing: 1px; }
  .contact__role { margin-bottom: 14px; }
  .contact__address { margin-bottom: 12px; }
  .contact__line { display: flex; align-items: center; gap: 10px; }
  .contact__line svg { width: 14px; height: 14px; flex: none; }
  .accent { color: var(--leaf-green); }
</style>
</head>
<body>
  <section class="card card--front">
    <div class="brand">
      <span class="brand__name">MOSLEN</span>
      <span class="brand__sub">ENVIRONMENTAL</span>
    </div>
    <ul class="services">
      <li>Contaminated Land</li>
      <li>Site Remediation</li>
      <li>Groundwater Assessment</li>
      <li>Health and Ecological Risk Assessments</li>
      <li>Acid Sulfate Soils</li>
      <li>Waste Classification</li>
    </ul>
  </section>

  <section class="card card--back">
    <div class="brand">
      <span class="brand__name">MOSLEN</span>
      <span class="brand__sub">ENVIRONMENTAL</span>
    </div>
    <div class="divider"></div>
    <div class="contact">
      <div class="contact__name">ROWAN TESSLER</div>
      <div class="contact__role">Project Engineer</div>
      <div class="contact__address">Level 3, Suite 3C<br>47-49 Dorrigan Lane<br>Wexmoor, NSW, 2188</div>
      <div class="contact__line">
        <svg viewBox="0 0 16 16" aria-hidden="true"><path fill="#6ab043" d="M3.6 1.2l2.3 2.9-1.4 1.6c.9 2 2.5 3.6 4.6 4.6l1.6-1.4 2.9 2.3-1.3 2.3C7.4 13.7 2.3 8.6 1.3 3z"/></svg>
        <span>(02 7314 2986)</span>
      </div>
      <div class="contact__line">
        <svg viewBox="0 0 16 16" aria-hidden="true"><rect x="1.5" y="3.5" width="13" height="9" rx="1" fill="none" stroke="#6ab043" stroke-width="1.6"/><path d="M2 4l6 5 6-5" fill="none" stroke="#6ab043" stroke-width="1.6"/></svg>
        <span>rowan@moslengreen.example</span>
      </div>
      <div class="contact__line">
        <svg viewBox="0 0 16 16" aria-hidden="true"><circle cx="8" cy="8" r="6.3" fill="none" stroke="#6ab043" stroke-width="1.5"/><path d="M1.7 8h12.6M8 1.7c-3 3.5-3 9.1 0 12.6M8 1.7c3 3.5 3 9.1 0 12.6" fill="none" stroke="#6ab043" stroke-width="1.2"/></svg>
        <span>www.<span class="accent">moslengreen</span>.example</span>
      </div>
    </div>
  </section>
</body>
</html>
```